New Business Card Design Project

Details for my new Business Card Design Project will be added soon. Like a nice simple design

Target Market(s)

Home improvement

Industry/Entity Type

Home Improvement

Contact Information for Business Card

Roofing siding gutters additions garages decks

Requirements
Must have
• Phone 5074629183
• Email morvantgc@quellmail.com

```html
<!DOCTYPE html>
<html lang="en">
<head>
<meta charset="utf-8">
<title>Handyman Services – Business Card</title>
<link rel="stylesheet" href="https://fonts.googleapis.com/css2?family=Open+Sans:wght@700&family=Fira+Sans+Extra+Condensed:ital,wght@1,600&display=swap">
<style>
  :root {
    --navy: #2d2a88;
    --roof-red: #c0172a;
    --roof-tint: #f4d3d7;
    --ladder-grey: #8c8c8c;
    --ladder-tint: #d9d9d9;
    --ink: #111111;
    --paper: #ffffff;
  }
  html, body {
    margin: 0;
    padding: 0;
    width: 1200px;
    height: 720px;
    overflow: hidden;
    background: var(--paper);
  }
  .business-card {
    display: block;
    width: 1200px;
    height: 720px;
  }
  .brand-title {
    font-family: "Open Sans", Arial, sans-serif;
    font-weight: 700;
    font-size: 80px;
    fill: var(--navy);
  }
  .services-line {
    font-family: "Fira Sans Extra Condensed", "Arial Narrow", sans-serif;
    font-style: italic;
    font-weight: 600;
    font-size: 62px;
    fill: var(--ink);
  }
  .contact-text {
    font-family: "Open Sans", Arial, sans-serif;
    font-weight: 700;
    font-size: 50px;
    fill: var(--navy);
  }
  .rooflines-area { fill: url(#roof-tone); }
  .ladder-area { fill: url(#ladder-tone); }
  .contact-icon { fill: var(--navy); }
  .contact-icon-outline { fill: none; stroke: var(--paper); stroke-width: 2.5; }
</style>
</head>
<body>
<svg class="business-card" viewBox="0 0 1200 720" xmlns="http://www.w3.org/2000/svg" aria-label="Handyman Services business card">
  <defs>
    <linearGradient id="roof-tone" x1="0" y1="0" x2="0" y2="1">
      <stop offset="0" stop-color="var(--roof-tint)"/>
      <stop offset="1" stop-color="var(--paper)"/>
    </linearGradient>
    <linearGradient id="ladder-tone" x1="0" y1="0" x2="1" y2="0">
      <stop offset="0" stop-color="var(--ladder-tint)"/>
      <stop offset="1" stop-color="#eeeeee"/>
    </linearGradient>
  </defs>

  <text class="brand-title" x="238" y="117" textLength="736" lengthAdjust="spacingAndGlyphs">Handyman Services</text>

  <rect class="rooflines-area" x="110" y="160" width="965" height="180" role="img" aria-label="Illustration of three red house rooflines in a row"/>

  <rect class="ladder-area" x="38" y="20" width="61" height="690" role="img" aria-label="Illustration of a grey ladder standing along the left edge"/>

  <text class="services-line" x="135" y="412" textLength="1025" lengthAdjust="spacingAndGlyphs">Roofing, siding, gutters, additions, garages decks</text>

  <g class="contact-row phone">
    <path class="contact-icon" d="M333,522 l8,-3 l7,13 l-6,5 q2,8 9,15 l7,-4 l9,12 l-6,4 q-9,3 -18,-9 q-12,-17 -10,-33 z"/>
    <text class="contact-text" x="439" y="565" textLength="344" lengthAdjust="spacingAndGlyphs">507-462-9183</text>
  </g>

  <g class="contact-row email">
    <path class="contact-icon" d="M326,628 l18,-12 l18,12 v20 h-36 z"/>
    <polyline class="contact-icon-outline" points="326,628 344,640 362,628"/>
    <polyline class="contact-icon-outline" points="326,648 339,636"/>
    <polyline class="contact-icon-outline" points="362,648 349,636"/>
    <text class="contact-text" x="437" y="648" textLength="600" lengthAdjust="spacingAndGlyphs">morvantgc@quellmail.com</text>
  </g>
</svg>
</body>
</html>
```